Brochure Projecct

I need a brochure created for my company, which will be sent to customers via email in PDF format. I have uploaded the company logo with this project, which I want incorporated in the design.

Designers should view the company website at www.brightcounselpages.com. I want the brochure to compliment the website (i.e., very clean design). I would also like pictures added to the brochure to make the design visually stunning.

In terms of content, I need four pages in the brochure to add four separate sections of content (one section per page). The four sections of content will be as follows (1) Search Engine Optimization Benefits (2) Increased Client Retention (3) Showcase Your Law Firm (4) Maximize Your Online ROI (5) Pricing Plans. I will give the content to the winning designer to add to the project. Each individual content section will have four subsection titles after which content of approximately 100 to 200 words will appear.

Designers can decide if other pages should be added to the brochure (i.e., a "cover page" that would have little content, but be visually appealing like the cover of a book - - - a "back page" that may just have the logo, contact information, etc).

My company address and email address should be prominently featured through every page (address: 2715 West Juniper Avenue, Suite 1400, Scottsdale, Arizona 85317; email: sales@brightcounselpages.com).

Industry/Entity Type

It Company

Requirements
Must have
• Clean look but visually stunning incorporating the design of the website at brightcounselpages.com as well as the logo. Also, room for content as set forth in the description of this project.

```html
<!DOCTYPE html>
<html lang="en">
<head>
<meta charset="utf-8">
<title>Increased Client Retention – Bright Counsel Pages</title>
<link rel="stylesheet" href="https://fonts.googleapis.com/css2?family=Open+Sans:wght@300;400;700;800&display=swap">
<style>
  :root {
    --stage: #5a5a5a;
    --paper: #ffffff;
    --wall-light: #b9b9b7;
    --wall-dark: #7f7f7d;
    --floor: #8a8a88;
    --bar-red: #c8363f;
    --headline-red: #d21f2b;
    --ink: #1a1a1a;
    --panel-top: #a3a3a5;
    --panel-bottom: #5b5b5e;
    --panel-text: #ffffff;
    --band-blue: #35679e;
    --band-text: #93b1d2;
  }
  * { margin: 0; padding: 0; box-sizing: border-box; }
  html, body {
    width: 1200px; height: 639px; overflow: hidden;
    background: var(--stage);
    font-family: "Open Sans", Arial, sans-serif;
  }
  .page {
    position: absolute; left: 57px; top: 43px;
    width: 1093px; height: 546px;
    background: var(--paper);
  }
  .hero {
    position: absolute; left: 0; top: 0;
    width: 881px; height: 480px;
    background:
      linear-gradient(180deg, transparent 84%, rgba(0,0,0,.12) 100%),
      radial-gradient(ellipse at 45% 40%, var(--wall-light) 0%, var(--wall-dark) 100%);
    overflow: hidden;
  }
  .hero svg { position: absolute; left: 0; top: 0; }
  .headline {
    position: absolute; left: 88px; top: 74px;
    line-height: 1;
  }
  .headline .accent {
    display: block;
    font-weight: 800; font-size: 41px; letter-spacing: -0.5px;
    color: var(--headline-red);
  }
  .headline .main {
    display: block; margin-top: 5px;
    font-weight: 300; font-size: 42px; letter-spacing: -0.5px;
    color: var(--ink);
  }
  .intro {
    position: absolute; left: 88px; top: 170px; width: 350px;
    font-size: 10.6px; line-height: 13.2px; color: var(--ink);
  }
  .about-panel {
    position: absolute; left: 890px; top: 0;
    width: 203px; height: 480px;
    background: linear-gradient(180deg, var(--panel-top), var(--panel-bottom));
    padding: 28px 12px 0 11px;
    color: var(--panel-text);
    font-size: 10.4px; line-height: 13.1px;
  }
  .about-panel p + p { margin-top: 13px; }
  .about-panel strong { font-weight: 700; }
  .contact-band {
    position: absolute; left: 0; top: 488px;
    width: 1093px; height: 58px;
    background: var(--band-blue);
    color: var(--band-text);
  }
  .contact-band .label {
    position: absolute; left: 29px; top: 11px;
    font-size: 14px; font-weight: 400;
  }
  .contact-band .address {
    position: absolute; left: 29px; top: 29px;
    font-size: 12px;
  }
  .contact-band .email {
    position: absolute; left: 742px; top: 26px;
    font-size: 12.5px;
  }
</style>
</head>
<body>
  <main class="page">
    <section class="hero">
      <svg width="881" height="480" viewBox="0 0 881 480" role="img"
           aria-label="Photo of a concrete wall with rising red bars and a businessman lifting the tallest bar">
        <g fill="var(--bar-red)">
          <rect x="118" y="363" width="37" height="105"/>
          <rect x="208" y="324" width="37" height="145"/>
          <rect x="299" y="304" width="36" height="166"/>
          <rect x="400" y="276" width="37" height="194"/>
          <rect x="501" y="234" width="37" height="237"/>
          <rect x="599" y="193" width="36" height="278"/>
          <rect x="693" y="0" width="36" height="133"/>
        </g>
      </svg>
      <h1 class="headline">
        <span class="accent">INCREASED</span>
        <span class="main">CLIENT RETENTION</span>
      </h1>
      <p class="intro">The Bright Counsel Pages is different from every other law firm directory website because we have already done the difficult work to differentiate between the hundreds of lawyers on the internet to locate an experienced attorney for your particular case.</p>
    </section>

    <aside class="about-panel">
      <p><strong>BRIGHT COUNSEL PAGES WAS CREATED BY AN ATTORNEY</strong> who realized he was able to guide his own friends, family, and even his own clients to the best lawyers in other practice areas. As importantly, he was also able to steer his trusted friends and family away from lawyers and law firms that were not as capable. He was able to provide that valuable guidance because he practices law in the same legal community and is, therefore, knowledgeable based upon that experience as to which lawyers produce the best results for their clients.</p>
      <p><strong>UNDERSTANDING EVERYONE DOES NOT HAVE A LAWYER</strong> in the family to help them locate an attorney, he started Bright Counsel Pages to ensure everyone has access to finding the best lawyer for his or her case. Instead of scrolling through dozens and dozens of pretty websites containing all sorts of marketing messages, Bright Counsel Pages allows you to evaluate several qualified lawyers who have an established reputation of excelling in their legal practice area. Capable advocates for their clients.</p>
    </aside>

    <footer class="contact-band">
      <span class="label">CONTACTS:</span>
      <span class="address">2715 West Juniper Avenue, Suite 1400, Scottsdale, Arizona 85317</span>
      <span class="email">email: sales@brightcounselpages.com</span>
    </footer>
  </main>
</body>
</html>
```